Design a 6 to 9 page Capability Statement

Project Overview
Veridane Systems requires a professionally designed Capability Statement that serves as a polished, leave-behind document for prospective clients and tender submissions. The finished document should clearly articulate who Veridane is, what we do, and the depth of expertise we bring — positioning us as Australia's leading specialist Qorvanth Systems Integrator in Data, AI, and the Modern Workplace.
All written content for this document has been provided in a separate Word document (Veridane_Capabilities.docx). The designer's responsibility is to bring this content to life through considered layout, typography, and visual design — not to rewrite or edit the copy.

Document Specifications

Format: A4, portrait orientation
Length: Approximately 6–8 pages
Intended output: Print-ready PDF and a digital/screen-optimised PDF
Primary use: Client-facing tender submissions, business development meetings, and digital distribution

Brand & Visual Direction
Source of Truth
The Veridane Systems website — https://veridane.example — is the definitive brand reference for this project. The designer should review the site thoroughly before commencing work. All design decisions should feel like a natural extension of the website's visual language.
Colour Palette
The design must reflect the Veridane brand while also communicating credibility, technical authority, and trustworthiness. We would like the designer to develop a palette using the following as a guide:

Primary Brand Red — As used in the Veridane logo. Use as an accent, highlight colour, and for key headings or section markers. Do not over-use; it should feel intentional and bold.
Deep Navy or Dark Blue — To convey corporate credibility and trust. Suitable for section backgrounds, large headers, or primary body text anchoring.
Teal / Mid-Blue-Green — A secondary accent to complement both the red and navy. Can be used for icons, dividers, callout boxes, or infographic elements.
White and Light Grey — For content areas, breathing space, and backgrounds to keep the layout clean and professional.
Dark Charcoal — For body copy to ensure readability without the harshness of full black.

The overall effect should feel modern, premium, and grounded — not loud or over-designed. Think: confident technology partner, not startup pitch deck.
Typography
Match the font style and weighting used on the Veridane website. Clean, modern sans-serif typefaces are preferred. There should be a clear typographic hierarchy — a strong heading weight for section titles, a medium weight for subheadings, and a regular/light weight for body copy. Font sizing should ensure comfortable reading in both print and digital formats.
Imagery & Icons

Use clean, professional iconography (flat or line-icon style) to support service categories and key statistics.
Any photography used should be consistent with the modern, professional tone seen on the website — aspirational tech/workplace imagery, not generic stock.
Qorvanth partnership badges and the Veridane logo must be used correctly and positioned with appropriate clear space.
The Harbor Guild logo/branding may appear where contextually relevant but must not compete with the Veridane brand.

Structural Reference: Harbor Guild Capability Statement
A Capability Statement from the Harbor Guild (a group of Qorvanth partner organisations of which Veridane is a founding member) is provided as a structural reference only. The designer should use it to understand general layout conventions for this type of document — such as how content sections flow, how case studies are presented, and how credentials and partnerships are displayed.
Important: The final Veridane Capability Statement must be entirely distinct from the Harbor Guild document in terms of design, branding, and visual execution. It is Veridane-branded, Veridane-focused, and must not look like a derivative or reskinned version of any partner document.

Content Structure (Based on Provided Word Document)
The following sections are to be designed and laid out from the content provided. The designer may adjust the flow between sections for optimal layout balance, but all content must be represented:

Cover Page
Veridane logo, document title ("Capability Statement"), a strong hero visual or graphic element, and contact/website details.
About Veridane Systems
Company overview — founded 2006, Qorvanth Solutions Partner, vision and values, office locations (Sydney, Melbourne, Dublin).
Our Qorvanth Partnership
Partner credentials — 12 Specialisations across 6 Solution Partner areas. Consider displaying Qorvanth partnership badges prominently here.
Core Service Capabilities
Four practice areas to be displayed clearly, potentially as a visual grid or icon-led layout:

Modern Work
Data & AI
Custom Applications
Managed Services

The Harbor Guild
Brief section on Veridane' founding membership and how this extends capability.
Q365 Pathfinder & AI Capability
Detailed section on Veridane' AI delivery experience — including the AI Kilnworks platform, Zelto product, and governance-led Pathfinder enablement approach.
Data & Integration Capability
Section covering the Junction Deck platform and Qorvanth Lattice expertise.
Case Studies
Multiple case studies drawn from the content document. These should be designed to scan quickly — with clear client name, a short outcome summary, and key deliverables. Full case study prose is available in the Word document. Suggested clients to feature:

KVLD (Zelto / KVL4)
Ashcombe Grammar
Brindle Ridge Airfield
Hearthway Relief
The Barrister Guild of Ostrava
Quay Board of Ostrava

Industries We Serve
Visual representation of the six key sectors: Education, Not-for-Profit, Health & Aged Care, Public Sector, Professional Services, Financial Services.
Contact & Next Steps
Back page or final section with full contact details, office locations, website URL, and a clear call to action.

Tone & Feel
The finished document should feel like it belongs on the desk of a CIO, CFO, or Procurement Manager at an enterprise or government organisation. It needs to convey:

Expertise — We are specialists, not generalists.
Trustworthiness — We work in regulated, complex environments.
Innovation — We are at the forefront of AI and cloud.
Partnership — We are invested in client outcomes, not just deliverables.

Avoid overly decorative or consumer-facing aesthetics. This is a B2B, enterprise-grade document.

Target Market(s)

C Level Executives at mid market customers in Australia - with staff of 500 to 5000

Font styles to use
Serif

Colors
0054AA
0677BA
7BADD7
CADEEF
E8F1F8
00AB8E
00BBA5
67D7C9
C6EFE9
E9F9F6
EB3D1F
EC4F4E
F09395
F8D3D4
FCEDEE
A7469A
B969AE
D3A5CF
EDDBEB
F8F0F9
6B429C
8869AF
B7A5CE
E3DAEB
F3F0F8

Requirements
Should not have
• Any cartoon style imagery

```html
<!DOCTYPE html>
<html lang="en">
<head>
<meta charset="utf-8">
<title>Veridane Systems — Capability Statement</title>
<link rel="stylesheet" href="https://fonts.googleapis.com/css2?family=Montserrat:wght@400;600;700;800&family=Open+Sans:wght@400;600&display=swap">
<style>
:root{
  --navy:#0b1846;
  --navy-2:#122661;
  --blue:#0054AA;
  --blue-mid:#0677BA;
  --blue-soft:#CADEEF;
  --teal:#00AB8E;
  --red:#EB3D1F;
  --red-soft:#F8D3D4;
  --white:#ffffff;
  --grey:#eef1f6;
  --charcoal:#2b2f3a;
  --muted-light:rgba(255,255,255,.72);
  --stage:#f4f5f8;
}
*{box-sizing:border-box;margin:0;padding:0}
html,body{width:870px;height:1200px;overflow:hidden;background:var(--stage)}
body{font-family:"Open Sans",Arial,sans-serif}
.sheet-grid{
  width:870px;height:1200px;padding:15px;
  display:grid;grid-template-columns:repeat(3,270px);grid-template-rows:repeat(3,380px);gap:15px;
}
.page{position:relative;overflow:hidden;padding:18px 16px 22px;box-shadow:0 1px 4px rgba(10,20,60,.18)}
.page--dark{background:linear-gradient(160deg,var(--navy-2) 0%,var(--navy) 60%,#081235 100%);color:var(--white)}
.page--light{background:var(--white);color:var(--charcoal)}
.photo{position:absolute;left:0;right:0}
.heading{font-family:"Montserrat",Arial,sans-serif;font-weight:800;text-transform:uppercase;letter-spacing:.02em;font-size:10px}
.heading--red{color:var(--red)}
.heading-rule{width:26px;height:2px;background:var(--red);margin:4px 0 8px}
.subhead{font-family:"Montserrat",Arial,sans-serif;font-weight:700;font-size:5.4px;margin-bottom:2px}
.copy{font-size:4.2px;line-height:1.55}
.page--dark .copy{color:var(--muted-light)}
.page--light .copy{color:#555b68}
.red-bar{background:var(--red);color:var(--white);font-family:"Montserrat",Arial,sans-serif;font-weight:700;font-size:5.6px;padding:3px 5px;margin:6px 0 5px}
.page-footer{position:absolute;left:16px;right:16px;bottom:8px;display:flex;justify-content:space-between;align-items:center;font-size:3.6px;opacity:.7}
.page-number{background:var(--red);color:var(--white);font-weight:700;padding:1px 4px;opacity:1}
/* cover */
.brand{display:flex;align-items:center;gap:3px;font-family:"Montserrat",Arial,sans-serif;font-weight:800;font-size:13px;color:var(--white);position:relative;z-index:2}
.brand-dot{width:6px;height:6px;background:var(--red)}
.cover-title{position:absolute;left:16px;top:196px;font-family:"Montserrat",Arial,sans-serif;font-weight:800;font-size:24px;line-height:1.05}
.cover-title span{color:var(--red);display:block}
.cover-icons{position:absolute;left:16px;top:256px;display:flex;gap:10px}
.cover-icon{display:flex;flex-direction:column;align-items:center;gap:2px;font-size:3.8px;color:var(--muted-light)}
.cover-icon i{width:12px;height:12px;border:1px solid var(--red);border-radius:50%;display:block}
.stats{position:absolute;left:16px;right:16px;top:290px;display:flex;gap:14px}
.stat b{display:block;font-family:"Montserrat",Arial,sans-serif;font-size:13px;font-weight:800}
.stat small{font-size:3.8px;color:var(--muted-light)}
.badges{position:absolute;left:16px;right:16px;bottom:18px;display:flex;align-items:center;gap:5px}
.badge{width:34px;height:14px;background:rgba(255,255,255,.9);border-radius:1px}
.guild{margin-left:auto;font-family:"Montserrat",Arial,sans-serif;font-weight:700;font-size:5.5px}
/* rows */
.value-list{display:flex;flex-direction:column;gap:7px;margin-top:8px;width:130px}
.value{display:flex;gap:5px}
.value i{flex:none;width:11px;height:11px;border-radius:50%;background:var(--red);display:block}
.callout{position:absolute;right:14px;top:190px;width:96px;background:var(--red);padding:8px;font-family:"Montserrat",Arial,sans-serif;font-weight:700;font-size:6px;line-height:1.35}
.two-col{display:grid;grid-template-columns:1fr 1fr;gap:8px}
.table-row{display:grid;grid-template-columns:48px 1fr;gap:6px;padding:4px 0;border-bottom:.5px solid rgba(255,255,255,.18)}
.table-row .subhead{font-size:4.8px}
.heading-icon{display:flex;align-items:center;gap:5px}
.heading-icon i{width:12px;height:12px;border:1.2px solid var(--red);border-radius:2px;display:block}
.tab-group{position:relative;padding-left:16px;margin-bottom:10px}
.tab-label{position:absolute;left:0;top:0;bottom:0;width:11px;background:var(--red);color:var(--white);writing-mode:vertical-rl;transform:rotate(180deg);font-family:"Montserrat",Arial,sans-serif;font-weight:700;font-size:4.4px;text-align:center}
.box-head{background:var(--red);color:var(--white);font-family:"Montserrat",Arial,sans-serif;font-weight:700;font-size:4.6px;padding:2px 4px;margin-bottom:2px}
.sector{display:flex;gap:4px;align-items:flex-start;margin-bottom:5px}
.sector i{flex:none;width:9px;height:9px;background:var(--red);display:block}
.quote{background:rgba(255,255,255,.08);border-top:2px solid var(--red);padding:5px}
.lets-talk{font-family:"Montserrat",Arial,sans-serif;font-weight:800;font-size:12px;color:var(--white)}
.clients{display:flex;flex-wrap:wrap;gap:4px 8px;font-family:"Montserrat",Arial,sans-serif;font-weight:700;font-size:4.6px;color:var(--white)}
</style>
</head>
<body>
<main class="sheet-grid">

  <!-- Page 1: cover -->
  <section class="page page--dark">
    <div class="photo" style="top:0;height:200px;background:linear-gradient(180deg,#3b5e8c 0%,#22406e 55%,var(--navy) 100%)" role="img" aria-label="Colleagues collaborating around laptops in a modern office"></div>
    <div class="brand"><span class="brand-dot"></span>Veridane</div>
    <h1 class="cover-title">Capability<span>Statement</span></h1>
    <div class="cover-icons">
      <div class="cover-icon"><i></i>Data &amp; AI</div>
      <div class="cover-icon"><i></i>Modern Work</div>
      <div class="cover-icon"><i></i>Cloud Apps</div>
    </div>
    <div class="stats">
      <div class="stat"><b>20+</b><small>Years delivering</small></div>
      <div class="stat"><b>500+</b><small>Projects completed</small></div>
      <div class="stat"><b>12</b><small>Specialisations</small></div>
    </div>
    <div class="badges">
      <span class="badge"></span><span class="badge"></span><span class="badge"></span>
      <span class="guild">Harbor Guild</span>
    </div>
  </section>

  <!-- Page 2: about -->
  <section class="page page--dark">
    <h2 class="heading">About Veridane Systems</h2>
    <div class="heading-rule"></div>
    <p class="copy" style="width:130px">Founded in 2006, Veridane Systems is a Qorvanth Solutions Partner specialising in Data, AI and the Modern Workplace. We help mid-market organisations plan, build and run secure platforms that deliver measurable outcomes for their people and customers.</p>
    <div class="photo" style="top:30px;left:152px;right:14px;height:120px;background:linear-gradient(150deg,#4d6fa0,#1d3463)" role="img" aria-label="Team member presenting in a meeting room"></div>
    <div class="value-list">
      <div class="value"><i></i><div><p class="subhead">Core</p><p class="copy">Specialists in Qorvanth cloud, data and AI.</p></div></div>
      <div class="value"><i></i><div><p class="subhead">Certainty</p><p class="copy">Proven delivery in regulated, complex sectors.</p></div></div>
      <div class="value"><i></i><div><p class="subhead">Vision</p><p class="copy">Helping clients adopt AI safely and at pace.</p></div></div>
      <div class="value"><i></i><div><p class="subhead">Problem Solving</p><p class="copy">Practical answers to real business challenges.</p></div></div>
    </div>
    <div class="callout">Creative minds, enablers of customers to achieve their vision.</div>
    <p class="copy" style="margin-top:12px">Offices in Sydney, Melbourne and Dublin.</p>
    <footer class="page-footer"><span>veridane.example</span><span class="page-number">02</span></footer>
  </section>

  <!-- Page 3: services -->
  <section class="page page--dark">
    <h2 class="heading">Our Services &amp; Capabilities</h2>
    <div class="heading-rule"></div>
    <div class="red-bar">Qorvanth 365 &amp; Modern Work</div>
    <div class="two-col">
      <div><p class="subhead">Intranet &amp; Collaboration</p><p class="copy">Modern intranets, teamwork and records that connect staff across every site.</p></div>
      <div><p class="subhead">Q365 Pathfinder</p><p class="copy">Governance-led enablement so teams adopt AI with confidence and control.</p></div>
      <div><p class="subhead">Security &amp; Compliance</p><p class="copy">Identity, data protection and policy aligned to regulated environments.</p></div>
      <div><p class="subhead">Adoption &amp; Change</p><p class="copy">Training and champions programs that lift usage and return on value.</p></div>
    </div>
    <div class="red-bar">Data &amp; AI</div>
    <div class="two-col">
      <div><p class="subhead">Qorvanth Lattice</p><p class="copy">Unified analytics platforms built for scale, trust and speed.</p></div>
      <div><p class="subhead">AI Kilnworks</p><p class="copy">Custom agents and models grounded in your own data.</p></div>
    </div>
    <div class="red-bar">Custom Applications</div>
    <div class="two-col">
      <div><p class="subhead">Junction Deck</p><p class="copy">Integration hub linking core systems in real time.</p></div>
      <div><p class="subhead">Low-code Apps</p><p class="copy">Fast business apps that automate manual workflows.</p></div>
    </div>
    <div class="red-bar">Managed Services</div>
    <p class="copy">Ongoing support, monitoring and optimisation of your Qorvanth estate.</p>
    <footer class="page-footer"><span>veridane.example</span><span class="page-number">03</span></footer>
  </section>

  <!-- Page 4: data -->
  <section class="page page--dark">
    <div class="heading-icon"><i></i><h2 class="heading">Qorvanth Lattice &amp; Data</h2></div>
    <div class="heading-rule"></div>
    <div class="table-row"><p class="subhead">Data Strategy</p><p class="copy">Roadmaps that align data investment with business priorities and risk.</p></div>
    <div class="table-row"><p class="subhead">Lakehouse</p><p class="copy">Modern platforms that bring every source into one trusted layer.</p></div>
    <div class="table-row"><p class="subhead">Reporting</p><p class="copy">Dashboards that give leaders clear, timely insight into performance.</p></div>
    <div class="table-row"><p class="subhead">Governance</p><p class="copy">Catalogue, lineage and access controls built in from day one.</p></div>
    <div class="table-row"><p class="subhead">Migration</p><p class="copy">Low-risk moves from legacy warehouses to the cloud.</p></div>
    <div class="table-row"><p class="subhead">Junction Deck</p><p class="copy">Integration platform connecting finance, HR and operations.</p></div>
    <div class="photo" style="bottom:0;height:120px;background:linear-gradient(180deg,#1c3466,#2f5a8e)" role="img" aria-label="Analyst reviewing data dashboards on screens"></div>
  </section>

  <!-- Page 5: cloud -->
  <section class="page page--dark">
    <div class="heading-icon"><i></i><h2 class="heading">Nimbra &amp; AI Cloud Applications</h2></div>
    <div class="heading-rule"></div>
    <div class="table-row"><p class="subhead">Cloud Platform</p><p class="copy">Secure landing zones designed for growth and compliance.</p></div>
    <div class="table-row"><p class="subhead">AI Kilnworks</p><p class="copy">Build, test and deploy AI agents with full governance.</p></div>
    <div class="table-row"><p class="subhead">Zelto</p><p class="copy">Our conversational assistant trusted by large member bodies.</p></div>
    <div class="table-row"><p class="subhead">App Modernisation</p><p class="copy">Re-platform legacy apps to scalable cloud services.</p></div>
    <div class="table-row"><p class="subhead">DevOps</p><p class="copy">Automated pipelines for faster, safer releases.</p></div>
    <div class="photo" style="bottom:0;height:140px;background:linear-gradient(180deg,#203a70,#3a6397)" role="img" aria-label="Developer working with code on a laptop"></div>
  </section>

  <!-- Page 6: solutions -->
  <section class="page page--light">
    <h2 class="heading" style="color:var(--navy)">Our Solutions</h2>
    <div class="heading-rule"></div>
    <div class="tab-group">
      <div class="tab-label">Modern Work</div>
      <div class="two-col">
        <div><p class="subhead" style="color:var(--navy)">Digital Workplace</p><p class="copy">Intranets and collaboration hubs that unite staff and knowledge.</p></div>
        <div><p class="subhead" style="color:var(--navy)">Records &amp; Compliance</p><p class="copy">Automated retention and audit-ready information management.</p></div>
        <div><p class="subhead" style="color:var(--navy)">Pathfinder Readiness</p><p class="copy">Assess, secure and prepare data before AI rollout.</p></div>
        <div><p class="subhead" style="color:var(--navy)">Intelligent Automation</p><p class="copy">Remove manual steps with flows and smart forms.</p></div>
      </div>
    </div>
    <div class="tab-group">
      <div class="tab-label">Data &amp; AI</div>
      <div class="two-col">
        <div><p class="subhead" style="color:var(--navy)">Analytics Platform</p><p class="copy">A single source of truth across the organisation.</p></div>
        <div><p class="subhead" style="color:var(--navy)">AI Agents</p><p class="copy">Task-specific assistants grounded in business data.</p></div>
        <div><p class="subhead" style="color:var(--navy)">Data Quality</p><p class="copy">Clean, trusted data ready for reporting and AI.</p></div>
        <div><p class="subhead" style="color:var(--navy)">Integration</p><p class="copy">Connected systems through Junction Deck.</p></div>
      </div>
    </div>
    <div class="photo" style="bottom:0;height:105px;background:linear-gradient(180deg,#2a4a7e,var(--navy))" role="img" aria-label="Team discussing solutions around a table"></div>
  </section>

  <!-- Page 7: products & managed services -->
  <section class="page page--light">
    <h2 class="heading heading--red">Proprietary Products</h2>
    <div class="heading-rule"></div>
    <p class="copy" style="margin-bottom:6px">Products built by Veridane to speed delivery and lower cost for clients.</p>
    <div class="two-col">
      <div><div class="box-head">Zelto</div><p class="copy">AI assistant for member and customer service teams.</p></div>
      <div><div class="box-head">Junction Deck</div><p class="copy">Integration platform for real-time data exchange.</p></div>
      <div><div class="box-head">Intranet Accelerator</div><p class="copy">Launch a modern intranet in weeks, not months.</p></div>
      <div><div class="box-head">Governance Toolkit</div><p class="copy">Policies and controls for safe AI adoption.</p></div>
      <div><div class="box-head">Records Engine</div><p class="copy">Automated classification and retention rules.</p></div>
      <div><div class="box-head">Insight Packs</div><p class="copy">Ready-made dashboards for common sectors.</p></div>
    </div>
    <h2 class="heading heading--red" style="margin-top:14px">Managed Services</h2>
    <div class="heading-rule"></div>
    <p class="copy" style="margin-bottom:6px">Reliable, local support that keeps your platforms secure and improving.</p>
    <div class="two-col">
      <div><div class="box-head">Service Desk</div><p class="copy">Responsive help from certified engineers.</p></div>
      <div><div class="box-head">Platform Health</div><p class="copy">Proactive monitoring and patching.</p></div>
      <div><div class="box-head">Security Ops</div><p class="copy">Threat detection and response.</p></div>
      <div><div class="box-head">Optimisation</div><p class="copy">Monthly reviews and roadmap planning.</p></div>
    </div>
    <footer class="page-footer"><span>veridane.example</span><span class="page-number">07</span></footer>
  </section>

  <!-- Page 8: industries & credentials -->
  <section class="page page--light">
    <h2 class="heading heading--red">Industries We Serve</h2>
    <div class="heading-rule"></div>
    <div class="two-col">
      <div class="sector"><i></i><div><p class="subhead">Education</p><p class="copy">Schools and universities.</p></div></div>
      <div class="sector"><i></i><div><p class="subhead">Not-for-Profit</p><p class="copy">Charities and member bodies.</p></div></div>
      <div class="sector"><i></i><div><p class="subhead">Health &amp; Aged Care</p><p class="copy">Providers and care networks.</p></div></div>
      <div class="sector"><i></i><div><p class="subhead">Public Sector</p><p class="copy">Agencies and authorities.</p></div></div>
      <div class="sector"><i></i><div><p class="subhead">Professional Services</p><p class="copy">Legal and advisory firms.</p></div></div>
      <div class="sector"><i></i><div><p class="subhead">Financial Services</p><p class="copy">Insurers and mutuals.</p></div></div>
    </div>
    <h2 class="heading heading--red" style="margin-top:10px">Credentials &amp; Delivery Approach</h2>
    <div class="heading-rule"></div>
    <div class="two-col">
      <div>
        <p class="subhead">Delivery Methodology</p>
        <p class="copy">Discover, design, build and adopt — a proven four stage approach with clear governance, fixed milestones and regular reporting to stakeholders.</p>
        <p class="subhead" style="margin-top:5px">Quality &amp; Security</p>
        <p class="copy">Certified processes and secure delivery practices aligned to industry standards.</p>
      </div>
      <div>
        <p class="subhead">Credentials &amp; Certifications</p>
        <p class="copy">Qorvanth Solutions Partner across six areas with twelve specialisations, and a founding member of the Harbor Guild.</p>
        <p class="subhead" style="margin-top:5px">Our People</p>
        <p class="copy">Senior consultants and engineers with deep sector experience.</p>
      </div>
    </div>
    <footer class="page-footer"><span>veridane.example</span><span class="page-number">08</span></footer>
  </section>

  <!-- Page 9: clients & contact -->
  <section class="page page--dark">
    <div class="photo" style="top:0;height:150px;background:linear-gradient(180deg,#45679a 0%,#1d3466 70%,var(--navy) 100%)" role="img" aria-label="City office building at dusk"></div>
    <div style="position:relative;margin-top:132px">
      <h2 class="heading" style="text-align:center">What Our Clients Say</h2>
      <div class="heading-rule" style="margin:4px auto 8px"></div>
      <div style="display:grid;grid-template-columns:repeat(3,1fr);gap:5px">
        <div class="quote"><p class="copy">“Veridane delivered on time and beyond our expectations.”</p><p class="subhead" style="margin-top:3px">KVLD</p></div>
        <div class="quote"><p class="copy">“A true partner through our digital workplace journey.”</p><p class="subhead" style="margin-top:3px">Ashcombe Grammar</p></div>
        <div class="quote"><p class="copy">“Clear advice, strong governance and real results.”</p><p class="subhead" style="margin-top:3px">Hearthway Relief</p></div>
      </div>
      <h2 class="lets-talk" style="margin-top:14px">LET'S <span style="color:var(--red)">TALK</span></h2>
      <p class="copy" style="margin:4px 0 6px">Speak with our team about your next data, AI or modern work project.</p>
      <p class="copy">Sydney · Melbourne · Dublin</p>
      <p class="subhead" style="margin:3px 0 10px">veridane.example</p>
      <div class="clients">
        <span>Brindle Ridge Airfield</span><span>The Barrister Guild of Ostrava</span><span>Quay Board of Ostrava</span>
      </div>
    </div>
    <div class="badges">
      <span class="brand" style="font-size:9px"><span class="brand-dot"></span>Veridane</span>
      <span class="guild">Harbor Guild</span>
    </div>
  </section>

</main>
</body>
</html>
```